Business Card Design

Sports massage therapist
Would like to convey a simple message.
graphic of human anatomy/muscular system
colours: orange with white/and or grey
glossey

Industry/Entity Type

Business

Contact Information for Business Card

Rhona Whitlow
Soft Tissue Therapist
Sports and Remedial Massage
07915 468302
whitlow.rhona@mailbrook.co.uk

```html
<!DOCTYPE html>
<html lang="en">
<head>
<meta charset="utf-8">
<title>Sports and Remedial Massage – Business Card</title>
<link rel="stylesheet" href="https://fonts.googleapis.com/css2?family=Old+Standard+TT:wght@700&family=Arimo:wght@400&display=swap">
<style>
  :root {
    --backdrop: #e4e1dc;
    --card-white: #fbfbfb;
    --card-shade: #ececec;
    --frame-orange: #e2a12a;
    --frame-edge: #c8841a;
    --name-orange: #eeb43a;
    --ink: #2f2f2f;
    --ink-soft: #3a3a3a;
    --muscle-red: #d9674a;
    --muscle-light: #f0b39c;
  }
  * { margin: 0; padding: 0; box-sizing: border-box; }
  html, body {
    width: 1200px;
    height: 892px;
    overflow: hidden;
    background: var(--backdrop);
  }
  .business-card {
    position: absolute;
    left: 100px;
    top: 130px;
    width: 1000px;
    height: 632px;
    background: var(--frame-orange);
    border: 2px solid var(--frame-edge);
    padding: 14px;
    box-shadow: 0 10px 30px rgba(0,0,0,0.18);
  }
  .card-face {
    position: relative;
    width: 100%;
    height: 100%;
    background: radial-gradient(ellipse at 60% 45%, var(--card-white) 40%, var(--card-shade) 100%);
    overflow: hidden;
  }
  .anatomy-figure {
    position: absolute;
    left: 28px;
    top: 96px;
    width: 210px;
    height: 500px;
  }
  .practice-title {
    position: absolute;
    left: 150px;
    top: 26px;
    font-family: "Old Standard TT", "Times New Roman", serif;
    font-weight: 700;
    font-size: 60px;
    color: var(--ink);
    letter-spacing: 0.5px;
    white-space: nowrap;
  }
  .therapist-block {
    position: absolute;
    right: 40px;
    top: 210px;
    text-align: right;
  }
  .therapist-name {
    font-family: "Old Standard TT", "Times New Roman", serif;
    font-weight: 700;
    font-size: 58px;
    line-height: 1;
    color: var(--name-orange);
  }
  .therapist-role {
    font-family: "Arimo", Arial, sans-serif;
    font-size: 38px;
    line-height: 1.2;
    color: var(--ink);
  }
  .contact-list {
    position: absolute;
    right: 40px;
    top: 378px;
    list-style: none;
    text-align: right;
    font-family: "Arimo", Arial, sans-serif;
    font-size: 30px;
    color: var(--ink-soft);
  }
  .contact-list li {
    display: flex;
    align-items: center;
    justify-content: flex-end;
    gap: 26px;
    height: 52px;
  }
  .contact-icon {
    width: 26px;
    height: 26px;
    flex: none;
  }
</style>
</head>
<body>
  <div class="business-card">
    <div class="card-face">
      <svg class="anatomy-figure" role="img" aria-label="Illustration of the human muscular system, full standing figure" viewBox="0 0 210 500">
        <defs>
          <linearGradient id="muscleTone" x1="0" y1="0" x2="1" y2="1">
            <stop offset="0" stop-color="var(--muscle-light)"/>
            <stop offset="0.5" stop-color="var(--muscle-red)"/>
            <stop offset="1" stop-color="var(--muscle-light)"/>
          </linearGradient>
        </defs>
        <rect x="0" y="0" width="210" height="500" rx="60" fill="url(#muscleTone)" opacity="0.85"/>
      </svg>

      <h1 class="practice-title">Sports and Remedial Massage</h1>

      <div class="therapist-block">
        <p class="therapist-name">Rhona Whitlow</p>
        <p class="therapist-role">Soft Tissue Therapist</p>
      </div>

      <ul class="contact-list">
        <li>
          <span>07915 468302</span>
          <svg class="contact-icon" viewBox="0 0 26 26" aria-hidden="true">
            <rect width="26" height="26" fill="var(--ink)"/>
            <path d="M8 6h3l1.5 4-2 1.2a9 9 0 0 0 4.3 4.3L16 13.5l4 1.5v3a2 2 0 0 1-2 2A13 13 0 0 1 6 8a2 2 0 0 1 2-2z" fill="var(--card-white)"/>
          </svg>
        </li>
        <li>
          <span>whitlow.rhona@mailbrook.co.uk</span>
          <svg class="contact-icon" viewBox="0 0 26 26" aria-hidden="true">
            <rect width="26" height="26" fill="var(--ink)"/>
            <rect x="5" y="8" width="16" height="11" fill="none" stroke="var(--card-white)" stroke-width="1.6"/>
            <path d="M5 8l8 6 8-6" fill="none" stroke="var(--card-white)" stroke-width="1.6"/>
          </svg>
        </li>
      </ul>
    </div>
  </div>
</body>
</html>
```